Larkmoor Health- Core Values Graphic for Visual Appeal

I would like a poster that could take these written core values from our organization and create a graphic that we could use for our staff and employees. I would also like to incorporate our branding into this project. Thank you!

Target Market(s)

To helps patients and employees understand the core values of our organization

Industry/Entity Type

Healthcare

Requirements
Must have
• Match our branding
Nice to have
• Please use your creativity!
Should not have
• Overly complex/ busy

```html
<!DOCTYPE html>
<html lang="en">
<head>
<meta charset="utf-8">
<title>Larkmoor Health — Core Values</title>
<link href="https://fonts.googleapis.com/css2?family=Poppins:wght@400;500;700;800&display=swap" rel="stylesheet">
<style>
  :root {
    --page-bg: #0f2a44;
    --paper: #ffffff;
    --brand-blue: #29abe2;
    --charcoal: #444446;
    --ink: #3a3a3c;
    --photo-light: #a9d8ef;
    --photo-mid: #6fb6de;
    --photo-deep: #3d7fae;
  }
  * { margin: 0; padding: 0; box-sizing: border-box; }
  html, body { width: 1200px; height: 1200px; overflow: hidden; }
  body {
    background: var(--page-bg);
    font-family: "Poppins", sans-serif;
    position: relative;
  }
  .poster {
    position: absolute;
    left: 180px; top: 10px;
    width: 840px; height: 1180px;
    background: var(--paper);
    overflow: hidden;
  }
  .team-photo {
    position: absolute; left: 0; top: 0;
    width: 840px; height: 287px;
    background: linear-gradient(120deg, var(--photo-deep) 0%, var(--photo-light) 45%, var(--photo-mid) 100%);
  }
  .brand-seal {
    position: absolute;
    left: 319px; top: 172px;
    width: 218px; height: 218px;
    border-radius: 50%;
    background: var(--paper);
    display: flex; align-items: center; justify-content: center;
    text-align: center;
  }
  .brand-seal .brand-name {
    font-weight: 700;
    font-size: 24px;
    line-height: 1.15;
    color: var(--charcoal);
  }
  .connectors { position: absolute; left: 0; top: 0; }
  .values-hub {
    position: absolute;
    left: -17px; top: 610px;
    width: 236px; height: 236px;
    border-radius: 50%;
    background: var(--charcoal);
    color: #fff;
    text-align: center;
  }
  .values-hub .count {
    position: absolute; left: 0; right: 0; top: 8px;
    font-weight: 800; font-size: 118px; line-height: 1;
    color: var(--brand-blue);
    text-shadow: 3px 3px 0 #222;
  }
  .values-hub .word-core {
    position: absolute; left: 0; right: 0; top: 114px;
    font-weight: 800; font-size: 46px; line-height: 1;
    text-shadow: 2px 2px 0 #222;
  }
  .values-hub .word-values {
    position: absolute; left: 0; right: 0; top: 165px;
    font-weight: 400; font-size: 38px; line-height: 1;
    text-shadow: 2px 2px 0 #222;
  }
  .value {
    position: absolute; left: 243px; width: 572px;
  }
  .value-tag {
    position: relative; height: 36px; width: 221px;
  }
  .value-tag svg { position: absolute; left: 0; top: 0; }
  .value-tag .title {
    position: absolute; left: 79px; top: 2px;
    color: #fff; font-weight: 500; font-size: 24px; line-height: 32px;
  }
  .value-text {
    margin-top: 12px;
    padding-left: 5px;
    font-size: 13.1px;
    line-height: 22px;
    color: var(--ink);
    text-align: justify;
    font-weight: 500;
  }
  .footer-band-blue {
    position: absolute; left: 0; top: 1155px; width: 234px; height: 25px;
    background: var(--brand-blue);
  }
  .footer-band-dark {
    position: absolute; left: 248px; top: 1155px; width: 592px; height: 25px;
    background: var(--charcoal);
  }
</style>
</head>
<body>
<main class="poster">
  <div class="team-photo" role="img" aria-label="Team photo of six clinic staff in dark uniforms over a blue-tinted image of a spinal adjustment"></div>

  <div class="brand-seal">
    <div class="brand-name">Larkmoor<br>Health</div>
  </div>

  <svg class="connectors" width="840" height="1180" viewBox="0 0 840 1180">
    <circle cx="101" cy="728" r="129" fill="none" stroke="#444446" stroke-width="1.5"/>
    <g stroke="#444446" stroke-width="1.2">
      <line x1="109" y1="599" x2="248" y2="448"/>
      <line x1="202" y1="669" x2="248" y2="634"/>
      <line x1="210" y1="773" x2="246" y2="804"/>
      <line x1="122" y1="855" x2="243" y2="998"/>
    </g>
    <g fill="#444446">
      <circle cx="109" cy="599" r="7"/>
      <circle cx="202" cy="669" r="7"/>
      <circle cx="210" cy="773" r="7"/>
      <circle cx="122" cy="855" r="7"/>
    </g>
  </svg>

  <div class="values-hub">
    <div class="count">4</div>
    <div class="word-core">Core</div>
    <div class="word-values">Values</div>
  </div>

  <section class="value" style="top:412px">
    <div class="value-tag">
      <svg width="221" height="36" viewBox="0 0 221 36">
        <path d="M18 0 H221 A18 18 0 0 1 221 36 H48 L70 0Z" fill="#29abe2"/>
        <path d="M205 0 A18 18 0 0 1 205 36 H48 L70 0Z" fill="#29abe2"/>
        <path d="M18 0 H57 L66 18 L57 36 H18 A18 18 0 0 1 18 0Z" fill="#444446"/>
        <g fill="none" stroke="#fff" stroke-width="1.6">
          <circle cx="24" cy="20" r="3"/><circle cx="36" cy="20" r="3"/><circle cx="30" cy="10" r="3"/>
          <path d="M19 30 a5 5 0 0 1 10 0 M31 30 a5 5 0 0 1 10 0"/>
        </g>
      </svg>
      <span class="title">Family</span>
    </div>
    <p class="value-text">At the heart of our mission is the commitment to provide high-quality, affordable healthcare in a comforting and uplifting family-oriented environment. Just as our community is our extended family, every patient is a cherished member of our healthcare family. We treat each individual with the same care, compassion, and respect we would offer to our own loved ones.</p>
  </section>

  <section class="value" style="top:604px">
    <div class="value-tag">
      <svg width="221" height="36" viewBox="0 0 221 36">
        <path d="M205 0 A18 18 0 0 1 205 36 H48 L70 0Z" fill="#29abe2"/>
        <path d="M18 0 H57 L66 18 L57 36 H18 A18 18 0 0 1 18 0Z" fill="#444446"/>
        <g fill="none" stroke="#fff" stroke-width="1.8">
          <circle cx="29" cy="15" r="8"/>
          <path d="M25 15 l3 3 l5 -6"/>
          <path d="M24 22 l-3 9 l4 -2 l2 4 l2 -8 M34 22 l3 9 l-4 -2 l-2 4 l-2 -8"/>
        </g>
      </svg>
      <span class="title">Excellence</span>
    </div>
    <p class="value-text">In line with our goal, we aspire not only to alleviate pain but also to inspire patients to become active participants in their well-being. We believe in empowering our patients through education and compassion. Our pursuit of excellence is unwavering, driven by our dedication to continuously improve our services at every level, ensuring that our community receives nothing less than exceptional care.</p>
  </section>

  <section class="value" style="top:794px">
    <div class="value-tag">
      <svg width="221" height="36" viewBox="0 0 221 36">
        <path d="M205 0 A18 18 0 0 1 205 36 H48 L70 0Z" fill="#29abe2"/>
        <path d="M18 0 H57 L66 18 L57 36 H18 A18 18 0 0 1 18 0Z" fill="#444446"/>
        <g fill="none" stroke="#fff" stroke-width="1.8" stroke-linecap="round">
          <path d="M16 9 l6 -2 l6 5 l5 -4 l6 2"/>
          <path d="M22 12 l6 5 l4 -3"/>
          <path d="M16 29 h6 l5 -4 h10 l4 -4"/>
        </g>
      </svg>
      <span class="title">Integrity</span>
    </div>
    <p class="value-text">In our healthcare team, 'Integrity' is non-negotiable. Our purpose is deeply rooted in ethics, integrity, and professional standards. We operate with the utmost integrity in every aspect of our work, adhering to the highest ethical principles. We understand that trust is the foundation of healthcare, and we are committed to maintaining the trust our community places in us.</p>
  </section>

  <section class="value" style="top:986px">
    <div class="value-tag">
      <svg width="221" height="36" viewBox="0 0 221 36">
        <path d="M205 0 A18 18 0 0 1 205 36 H48 L70 0Z" fill="#29abe2"/>
        <path d="M18 0 H57 L66 18 L57 36 H18 A18 18 0 0 1 18 0Z" fill="#444446"/>
        <g fill="none" stroke="#fff" stroke-width="1.8" stroke-linecap="round">
          <circle cx="32" cy="13" r="7"/>
          <path d="M32 9 v8 M28 13 h8"/>
          <path d="M14 22 v9 M17 24 h6 l6 3 h6 l6 -4 M17 30 h14 l10 -6"/>
        </g>
      </svg>
      <span class="title">Service</span>
    </div>
    <p class="value-text">Our vision is grounded in the belief that every person possesses the innate potential for true health. We aim to facilitate the body's natural healing response by providing the highest level of service. Our hope for each patient extends beyond healing; we aspire to help you fulfill your life's mission and purpose abundantly, supporting you in your journey to well-being.</p>
  </section>

  <div class="footer-band-blue"></div>
  <div class="footer-band-dark"></div>
</main>
</body>
</html>
```